Dentist Home Page Design

We need a home page design to be used as a responsive wordpress theme for our dentist website. Website overall look and feel should look professional, yet very friendly as going to dentist is not people's favorite thing to do, for most it might even be scary. We want our website to differentiate with its design from all other generic looking cookie cutter dentists and creates a branded feel.
you can use a generic image for the 680x300px banner on the home pageif you like in the meantime). Total width should not exceed 960 px
Please follow the layout on the wireframes, do not add or delete random elements.
Target Market(s)
mostly targets male/female between 30-45, families with kids as well.
Industry/Entity Type
It Professional
Colors
Designer to choose colors to be used in the design.
Look and feel
Each slider illustrates characteristics of the customer's brand and the style your logo design should communicate.

```html
<!DOCTYPE html>
<html lang="en">
<head>
<meta charset="utf-8">
<title>Harbourside Dental – Home</title>
<link href="https://fonts.googleapis.com/css2?family=Open+Sans:wght@400;600;700;800&display=swap" rel="stylesheet">
<style>
:root{
  --brand:#1b9ad8;
  --brand-dark:#0d78b5;
  --sky:#e9f4fa;
  --line:#cfe3ee;
  --text:#555d63;
  --heading:#1b8fcf;
  --orange:#f2961d;
  --footer:#2a2c2e;
  --footer-text:#c9cdd0;
  --photo-a:#9cc7df;
  --photo-b:#d9b9a3;
}
*{box-sizing:border-box;margin:0;padding:0}
html,body{width:1200px;height:2384px;overflow:hidden}
body{font-family:"Open Sans",Arial,sans-serif;color:var(--text);background:linear-gradient(#f6fbfe,#ffffff 700px);position:relative}
.abs{position:absolute}
.photo{background:linear-gradient(135deg,var(--photo-a),var(--photo-b))}

/* header */
.site-header{left:0;top:0;width:1200px;height:216px}
.brand{left:48px;top:28px}
.brand-name{font-size:44px;font-weight:800;color:var(--brand-dark);letter-spacing:1px;display:flex;align-items:center;gap:12px;white-space:nowrap}
.brand-name i{width:22px;height:22px;border-radius:50%;background:var(--brand);display:inline-block}
.brand-doctor{font-size:22px;font-weight:700;color:var(--brand-dark);margin-top:6px;border-top:2px solid var(--line);padding-top:6px;width:340px}
.brand-roles{display:flex;justify-content:space-between;width:340px;font-size:12px;color:#7a8388;margin-top:2px}
.share-row{left:600px;top:28px;display:flex;gap:6px}
.share-row span{width:30px;height:16px;background:#d6e4ec;border-radius:2px}
.follow{right:48px;top:56px;display:flex;align-items:center;gap:8px;font-size:18px;color:var(--brand)}
.follow span{width:32px;height:32px;border-radius:5px;background:var(--brand)}
.follow span:nth-child(3){background:#3d8fd1}
.follow span:nth-child(4){background:#c9432f}
.call-btn{right:400px;top:120px;background:var(--brand);color:#fff;font-size:16px;font-weight:700;padding:8px 18px;border-radius:4px;white-space:nowrap}
.phone{right:48px;top:100px;font-size:46px;font-weight:700;color:var(--brand-dark);letter-spacing:-1px;white-space:nowrap;line-height:56px}
.phone-sub{right:48px;top:162px;font-size:16px;color:#6a7378;white-space:nowrap}

/* nav */
.main-nav{left:0;top:224px;width:1200px;height:44px;background:linear-gradient(var(--brand),var(--brand-dark));display:flex;padding-left:36px}
.main-nav a{color:#fff;font-size:16px;font-weight:700;text-decoration:none;padding:0 22px;line-height:44px;border-right:1px solid rgba(255,255,255,.35);white-space:nowrap}
.main-nav a:last-child{border-right:none}

/* hero */
.hero{left:40px;top:290px;width:730px;height:400px;border-radius:6px;border:4px solid #fff;box-shadow:0 2px 8px rgba(0,0,0,.12)}
.hero-dots{left:640px;top:660px;display:flex;gap:6px}
.hero-dots i{width:10px;height:10px;border-radius:50%;background:#fff;opacity:.7}
.consult{left:790px;top:290px;width:370px;height:400px;background:var(--sky);border:1px solid var(--line);border-radius:4px}
.consult h2{background:var(--brand);color:#fff;font-size:20px;font-weight:800;text-align:center;padding:10px 0}
.consult form{padding:14px 40px;display:flex;flex-direction:column;gap:9px}
.field{height:28px;background:#fff;border:1px solid var(--line);font-size:12px;color:#99a2a8;padding:6px 8px}
.field.area{height:74px}
.send{align-self:center;background:var(--brand);color:#fff;font-weight:700;font-size:16px;padding:6px 26px;border-radius:3px;margin-top:4px}

/* intro */
.intro-title{left:40px;top:730px;font-size:28px;font-weight:700;color:var(--heading);white-space:nowrap}
.intro-text{left:40px;top:776px;width:580px;font-size:14px;line-height:22px}
.video{left:640px;top:740px;width:520px;height:260px;background:var(--sky);border:1px solid var(--line);border-radius:4px}
.video svg{position:absolute;left:198px;top:68px}
.intro-wide{left:40px;top:1018px;width:1120px;font-size:14px;line-height:22px}

/* panels */
.panel{border:1px solid var(--line);background:#fff;border-radius:4px;overflow:hidden}
.panel-head{background:var(--brand);color:#fff;font-size:15px;font-weight:800;padding:7px 14px;display:flex;justify-content:space-between;align-items:center;height:34px}
.panel-head em{font-style:normal;font-size:12px;font-weight:600;text-decoration:underline}
.services{left:40px;top:1100px;width:352px;height:292px}
.services ul{list-style:none;display:grid;grid-template-columns:1fr 1fr 1fr;gap:10px 6px;padding:16px 12px;font-size:11.5px}
.services li{border-bottom:1px solid var(--line);padding-bottom:6px;white-space:nowrap}
.kids{left:424px;top:1100px;width:352px;height:292px}
.doctor{left:808px;top:1100px;width:352px;height:292px}
.panel-photo{height:256px}

.videos{left:40px;top:1440px;width:550px;height:330px}
.video-grid{display:grid;grid-template-columns:repeat(4,1fr);gap:12px;padding:14px}
.thumb-img{height:112px;border-radius:3px}
.thumb p{font-size:12px;text-align:center;margin-top:4px;line-height:16px;white-space:nowrap}
.cases{left:610px;top:1440px;width:550px;height:330px}
.case-grid{display:grid;grid-template-columns:1fr 1fr;gap:10px 16px;padding:12px 14px}
.case{position:relative;height:86px}
.case-pics{display:flex;gap:4px;height:66px}
.case-pics div{flex:1;border-radius:3px}
.case-pics .blank{background:var(--sky)}
.case-tag{position:absolute;left:0;top:6px;background:var(--orange);color:#fff;font-size:13px;font-weight:800;padding:3px 10px;white-space:nowrap}
.case p{font-size:11px;font-weight:700;text-align:center;margin-top:3px;line-height:16px;text-transform:uppercase;white-space:nowrap}

/* social strip */
.likes{left:40px;top:1800px;width:1120px;height:86px;border-top:1px solid var(--line);border-bottom:1px solid var(--line)}
.likes .line{position:absolute;left:0;top:8px;font-size:13px;display:flex;align-items:center;gap:8px}
.likes .line i{width:16px;height:16px;background:var(--brand-dark);display:inline-block}
.likes .link{position:absolute;right:0;top:8px;font-size:13px;color:var(--brand);text-decoration:underline}
.avatars{position:absolute;left:0;top:34px;display:flex;gap:6px}
.avatars span{width:42px;height:42px;border-radius:2px}

/* footer */
.site-footer{left:0;top:1912px;width:1200px;height:472px;background:var(--footer);color:var(--footer-text);font-size:13px;line-height:20px}
.fcol{position:absolute;top:30px}
.fcol h3{color:#fff;font-size:16px;font-weight:700;margin-bottom:8px}
.fcol a{color:var(--brand);text-decoration:underline}
.map{width:250px;height:180px;margin-top:8px;background:linear-gradient(135deg,#dfe6d8,#c8d6e0)}
.ffield{width:280px;height:30px;background:#fff;margin-top:8px;color:#999;padding:5px 8px}
.signup{display:inline-block;margin:12px 0 0 100px;background:var(--brand);color:#fff;font-weight:700;padding:5px 22px;border-radius:3px}
.legal{position:absolute;right:48px;top:400px;font-size:12px}
</style>
</head>
<body>

<header class="site-header abs">
  <div class="brand abs">
    <div class="brand-name"><i></i>Harbourside Dental</div>
    <div class="brand-doctor">Dr. Martin Kessler</div>
    <div class="brand-roles"><span>General Dentist</span><span>Orthodontics</span></div>
  </div>
  <div class="share-row abs"><span></span><span></span><span></span><span></span></div>
  <div class="follow abs">Follow us <span></span><span></span><span></span><span></span></div>
  <div class="call-btn abs">click to call</div>
  <div class="phone abs">(555) 014-2290</div>
  <div class="phone-sub abs">Request a Free Consultation</div>
</header>

<nav class="main-nav abs">
  <a>HOME</a><a>ABOUT</a><a>SERVICES</a><a>OUR TECHNOLOGY</a><a>DENTAL CARE</a><a>CASE STUDIES</a><a>NEW PATIENTS</a><a>CONTACT</a>
</nav>

<div class="hero abs photo" role="img" aria-label="Smiling patient in the dental chair with the dentist"></div>
<div class="hero-dots abs"><i></i><i></i><i></i><i></i></div>

<aside class="consult abs">
  <h2>REQUEST A FREE CONSULTATION</h2>
  <form>
    <div class="field">Full Name</div>
    <div class="field">Phone Number</div>
    <div class="field">Your Email</div>
    <div class="field">Preferred Date &amp; Time</div>
    <div class="field area">Your Message</div>
    <div class="send">SEND REQUEST</div>
  </form>
</aside>

<h1 class="intro-title abs">Your Experience in Dentistry Begins Now!</h1>
<p class="intro-text abs">Lorem ipsum dolor sit amet, consectetur adipisicing elit, sed do eiusmod tempor incididunt ut labore et dolore magna aliqua. Ut enim ad minim veniam, quis nostrud exercitation ullamco laboris nisi ut aliquip ex ea commodo consequat. Duis aute irure dolor in reprehenderit in voluptate velit esse cillum dolore eu fugiat nulla pariatur. Excepteur sint occaecat cupidatat non proident, sunt in culpa qui officia deserunt mollit anim id est laborum. Lorem ipsum dolor sit amet, consectetur adipisicing elit, sed do eiusmod tempor incididunt ut labore et dolore magna aliqua. Ut enim ad minim veniam, quis nostrud exercitation ullamco laboris nisi ut aliquip ex ea commodo consequat.</p>
<div class="video abs" role="img" aria-label="Welcome video from the practice">
  <svg width="124" height="124" viewBox="0 0 124 124"><circle cx="62" cy="62" r="58" fill="#fff" stroke="#1b9ad8" stroke-width="6"/><path d="M48 36 L90 62 L48 88 Z" fill="#1b9ad8"/></svg>
</div>
<p class="intro-wide abs">Lorem ipsum dolor sit amet, consectetur adipisicing elit, sed do eiusmod tempor incididunt ut labore et dolore magna aliqua. Ut enim ad minim veniam, quis nostrud exercitation ullamco laboris nisi ut aliquip ex ea commodo consequat. Duis aute irure dolor in reprehenderit in voluptate velit esse cillum dolore eu fugiat nulla pariatur. Excepteur sint occaecat cupidatat non proident.</p>

<section class="services panel abs">
  <div class="panel-head">OUR DENTAL SERVICES <em>view all</em></div>
  <ul>
    <li>General Dentistry</li><li>Cosmetic Dentistry</li><li>Clear Aligners</li>
    <li>Implants</li><li>Porcelain Veneers</li><li>Dental Veneers</li>
    <li>Root Canal</li><li>Smile Makeover</li><li>Dentures</li>
    <li>Dental Bonding</li><li>Thin Veneers</li><li>Whitening</li>
    <li>Dental Bridges</li><li>Crowns</li><li>Sedation</li>
  </ul>
</section>
<section class="kids panel abs">
  <div class="panel-head">DENTISTRY FOR YOUR KIDS</div>
  <div class="panel-photo photo" role="img" aria-label="Child having a check-up at the dentist"></div>
</section>
<section class="doctor panel abs">
  <div class="panel-head">MEET DR. MARTIN KESSLER</div>
  <div class="panel-photo photo" role="img" aria-label="Portrait of the dentist"></div>
</section>

<section class="videos panel abs">
  <div class="panel-head">DENTAL EDUCATIONAL VIDEOS <em>view all</em></div>
  <div class="video-grid">
    <div class="thumb"><div class="thumb-img photo" role="img" aria-label="Video still on dental implants"></div><p>Dental Implants</p></div>
    <div class="thumb"><div class="thumb-img photo" role="img" aria-label="Video still on veneers"></div><p>Veneers</p></div>
    <div class="thumb"><div class="thumb-img photo" role="img" aria-label="Video still on clear aligners"></div><p>Clear Aligners</p></div>
    <div class="thumb"><div class="thumb-img photo" role="img" aria-label="Video still on whitening"></div><p>Whitening</p></div>
    <div class="thumb"><div class="thumb-img photo" role="img" aria-label="Video still on orthodontics"></div><p>Orthodontics</p></div>
    <div class="thumb"><div class="thumb-img photo" role="img" aria-label="Video still on smile makeover"></div><p>Smile Makeover</p></div>
    <div class="thumb"><div class="thumb-img photo" role="img" aria-label="Video still on root canal"></div><p>Root Canal</p></div>
    <div class="thumb"><div class="thumb-img photo" role="img" aria-label="Video still on dental bridges"></div><p>Bridges</p></div>
  </div>
</section>

<section class="cases panel abs">
  <div class="panel-head">PATIENT CASE STUDIES <em>view all</em></div>
  <div class="case-grid">
    <div class="case"><div class="case-pics"><div class="blank"></div><div class="photo" role="img" aria-label="Smile after dentures"></div></div><span class="case-tag">CASE STUDY #1</span><p>Dentures</p></div>
    <div class="case"><div class="case-pics"><div class="blank"></div><div class="photo" role="img" aria-label="Smile after tooth replacement"></div></div><span class="case-tag">CASE STUDY #2</span><p>Tooth Replacement</p></div>
    <div class="case"><div class="case-pics"><div class="blank"></div><div class="photo" role="img" aria-label="Smile after makeover"></div></div><span class="case-tag">CASE STUDY #3</span><p>Smile Makeover</p></div>
    <div class="case"><div class="case-pics"><div class="blank"></div><div class="photo" role="img" aria-label="Smile after orthodontics"></div></div><span class="case-tag">CASE STUDY #4</span><p>Orthodontics</p></div>
    <div class="case"><div class="case-pics"><div class="blank"></div><div class="photo" role="img" aria-label="Smile after dental implants"></div></div><span class="case-tag">CASE STUDY #5</span><p>Dental Implants</p></div>
    <div class="case"><div class="case-pics"><div class="blank"></div><div class="photo" role="img" aria-label="Smile after whitening"></div></div><span class="case-tag">CASE STUDY #6</span><p>Tooth Whitening</p></div>
  </div>
</section>

<section class="likes abs">
  <div class="line"><i></i>Nora Fields, Ben Okafor and 2,904,571 others like this.</div>
  <a class="link">Like Us on Friendbook</a>
  <div class="avatars" role="img" aria-label="Profile pictures of followers">
    <span class="photo"></span><span class="photo"></span><span class="photo"></span><span class="photo"></span><span class="photo"></span><span class="photo"></span><span class="photo"></span><span class="photo"></span><span class="photo"></span><span class="photo"></span><span class="photo"></span><span class="photo"></span><span class="photo"></span><span class="photo"></span><span class="photo"></span><span class="photo"></span><span class="photo"></span><span class="photo"></span><span class="photo"></span><span class="photo"></span><span class="photo"></span><span class="photo"></span><span class="photo"></span>
  </div>
</section>

<footer class="site-footer abs">
  <div class="fcol" style="left:60px;width:300px">
    <h3>Contact Info &amp; Hours</h3>
    Phone: (555) 014-2290<br>Fax: (555) 014-2291<br><a>Email Us</a> · <a>Request Appointment</a><br><br>
    <b style="color:#fff">Office Hours</b><br>
    Monday: 10:00 am – 8 pm<br>Tuesday: 10:00 am – 6 pm<br>Wednesday: 10:00 am – 8 pm<br>Thursday: 9:00 am – 5 pm<br>Friday: Closed<br>Saturday: 10:00 am – 2:00 pm<br>Sunday: Closed<br><br>
    Follow Us<br><a>Chirper</a> <a>Friendbook</a> <a>ClipTube</a><br><a>Take Our Survey</a>
  </div>
  <div class="fcol" style="left:360px;width:300px">
    <h3>Address &amp; Directions</h3>
    Harbourside Dental<br>1200 Harbour Street East,<br>Lakeview, ON L1N 2L3<br>(Free Parking in the Front)
    <div class="map" role="img" aria-label="Street map showing the office location"></div>
  </div>
  <div class="fcol" style="left:760px;width:380px">
    <h3>Sign-Up for Our Monthly Newsletter</h3>
    To receive free dental health tips from Dr. Kessler.
    <div class="ffield">First Name</div>
    <div class="ffield">Email Address</div>
    <div class="ffield">Mobile Phone</div>
    <div class="signup">SIGN UP</div>
  </div>
  <div class="legal">Terms of Service &nbsp;|&nbsp; Privacy Policy &nbsp;|&nbsp; Site Map</div>
</footer>

</body>
</html>
```